Kalmoret Windham & Associates

We would like a simple, professional business card using a similar font to our logo.

Industry/Entity Type

Law Firm

Contact Information for Business Card

Martin Kalmoret, Esq. 47 Tillman Lane, 2nd Floor Brantwell, MA 02199 Office: 781.555.0143 Cell: 508.555.0196 Email: marty@kwfirmma.com kalmoretwindhamlaw.com

Font styles to use
Other font styles liked:
• We would like to use the fonts used in the logo or similar

Colors
0054AA
0677BA
7BADD7
CADEEF
E8F1F8

Requirements
Must have
• We would like the fonts to match the logo
Nice to have
• not too much design- very simple and professional business card. I added a picture of a business card that I tried to start but I am not a designer! Hopefully it will help with the address and phone numbers and kind of what we are looking for.

```html
<!DOCTYPE html>
<html lang="en">
<head>
<meta charset="utf-8">
<title>Kalmoret Windham &amp; Associates – Business Card</title>
<link rel="stylesheet" href="https://fonts.googleapis.com/css2?family=Cinzel:wght@500&family=Arimo:wght@400&display=swap">
<style>
  :root {
    --navy: #1f3770;
    --band: #2a3f78;
    --rule: #6b6b6b;
    --ink: #555a60;
    --card: #ffffff;
    --backdrop: #ececec;
  }
  html, body {
    margin: 0;
    padding: 0;
    width: 1200px;
    height: 991px;
    overflow: hidden;
    background: var(--backdrop);
  }
  .canvas {
    position: relative;
    width: 1200px;
    height: 991px;
  }
  .card {
    position: absolute;
    width: 424px;
    height: 242px;
    background: var(--card);
    box-shadow: 0 2px 6px rgba(0,0,0,0.12);
    overflow: hidden;
  }
  .card--front { left: 300px; top: 240px; }
  .card--back  { left: 502px; top: 542px; }

  .brand-square {
    position: absolute;
    background: var(--navy);
  }
  .brand-rule {
    position: absolute;
    width: 1.5px;
    background: var(--rule);
  }
  .brand-name {
    position: absolute;
    margin: 0;
    font-family: "Cinzel", serif;
    font-weight: 500;
    color: var(--navy);
    line-height: 1;
    white-space: nowrap;
  }
  .brand-name span { display: block; }

  .card--front .brand-square { left: 122px; top: 86px; width: 69px; height: 69px; }
  .card--front .brand-rule { left: 204px; top: 73px; height: 94px; }
  .card--front .brand-name { left: 217px; top: 88px; font-size: 21px; }
  .card--front .brand-name span + span { margin-top: 2px; }
  .card--front .brand-name .tag { font-size: 15px; letter-spacing: 1px; margin-top: 4px; }

  .card--back .brand-square { left: 51px; top: 26px; width: 43px; height: 43px; }
  .card--back .brand-rule { left: 102px; top: 18px; height: 59px; }
  .card--back .brand-name { left: 109px; top: 29px; font-size: 13px; }
  .card--back .brand-name span + span { margin-top: 1px; }
  .card--back .brand-name .tag { font-size: 9.5px; letter-spacing: 0.8px; margin-top: 3px; }

  .person-name {
    position: absolute;
    left: 100px;
    top: 108px;
    margin: 0;
    font-family: "Cinzel", serif;
    font-weight: 500;
    font-size: 23px;
    color: var(--navy);
    white-space: nowrap;
  }

  .contact {
    position: absolute;
    font-family: "Arimo", sans-serif;
    font-size: 10px;
    line-height: 11.5px;
    color: var(--ink);
    white-space: nowrap;
    font-style: normal;
  }
  .contact svg { width: 8px; height: 8px; fill: var(--navy); flex: none; }
  .contact-row { display: flex; align-items: center; gap: 4px; }
  .contact-row .gap { width: 3px; }
  .contact--address { left: 99px; top: 192px; display: flex; gap: 5px; align-items: flex-start; }
  .contact--address svg { margin-top: 2px; width: 8px; height: 10px; }
  .contact--lines { left: 255px; top: 180px; }

  .card-band {
    position: absolute;
    left: 0;
    bottom: 0;
    width: 100%;
    height: 14px;
    background: var(--band);
  }
</style>
</head>
<body>
<main class="canvas">

  <section class="card card--front" aria-label="Card front">
    <div class="brand-square"></div>
    <div class="brand-rule"></div>
    <h1 class="brand-name"><span>Kalmoret</span><span>Windham</span><span class="tag">&amp; Associates</span></h1>
  </section>

  <section class="card card--back" aria-label="Card back">
    <div class="brand-square"></div>
    <div class="brand-rule"></div>
    <p class="brand-name"><span>Kalmoret</span><span>Windham</span><span class="tag">&amp; Associates</span></p>

    <h2 class="person-name">Martin Kalmoret, Esq.</h2>

    <address class="contact contact--address">
      <svg viewBox="0 0 10 14" aria-hidden="true"><path d="M5 0a5 5 0 0 0-5 5c0 3.5 5 9 5 9s5-5.5 5-9a5 5 0 0 0-5-5zm0 7a2 2 0 1 1 0-4 2 2 0 0 1 0 4z"/></svg>
      <span>47 Tillman Lane, 2nd<br>Floor Brantwell, MA 02199</span>
    </address>

    <div class="contact contact--lines">
      <div class="contact-row">
        <svg viewBox="0 0 10 10" aria-hidden="true"><path d="M2 0l2 2.5-1 1.3c.6 1.3 1.6 2.3 2.9 2.9l1.3-1L10 7.7 8.6 10C4 10 0 6 0 1.4z"/></svg>
        <span>781.555.0143</span><span class="gap"></span>
        <svg viewBox="0 0 10 10" aria-hidden="true"><path d="M2.5 0h5v10h-5zM3.5 1v7h3V1z"/></svg>
        <span>508.555.0196</span>
      </div>
      <div class="contact-row">
        <svg viewBox="0 0 10 10" aria-hidden="true"><path d="M0 2h10v6H0zM1 3l4 3 4-3"/></svg>
        <span>marty@kwfirmma.com</span>
      </div>
      <div class="contact-row">
        <svg viewBox="0 0 10 10" aria-hidden="true"><circle cx="5" cy="5" r="4.5"/></svg>
        <span>kalmoretwindhamlaw.com</span>
      </div>
    </div>

    <div class="card-band"></div>
  </section>

</main>
</body>
</html>
```